Young Balance Support Network

We need a poster explaining that some children live with a disability called Vestibular Disorder. Feel free to ask question. We want you to respect our color code, same as our logo.

Here is our website : http://www.ybsnetwork.org/

We need to sensibilise people about this disability for children.

Industry/Entity Type

Charity

Font styles to use
Serif

Requirements
Must have
• 1. our logo (with all our details) + one of the photo of Marek
• 2. design showing a child with a dizziness for exemple
• 3. a title saying : Aidez-nous à changer la vie des enfants vivant avec un problème vestibulaire
• 4.include the text attached (information flyer YBSN)
• Poster size : 24"X 36"
Should not have
• wheel chair

```html
<!DOCTYPE html>
<html lang="fr">
<head>
<meta charset="utf-8">
<title>YBSN – Aidez-nous à changer la vie des enfants</title>
<link href="https://fonts.googleapis.com/css2?family=Lato:wght@400;700;900&display=swap" rel="stylesheet">
<style>
  :root {
    --sky: #56bde9;
    --sky-dark: #2f93c4;
    --sky-pale: #d2eaf8;
    --lime: #c2d530;
    --orange: #f5b234;
    --ink: #1f1f1f;
    --red: #e0262b;
    --white: #ffffff;
  }
  * { margin: 0; padding: 0; box-sizing: border-box; }
  html, body { width: 797px; height: 1200px; overflow: hidden; background: var(--white); }
  .poster {
    position: relative; width: 797px; height: 1200px; overflow: hidden;
    font-family: "Lato", sans-serif; color: var(--ink); background: var(--white);
  }
  .hero-photo {
    position: absolute; left: 0; top: 0; width: 797px; height: 450px;
    background:
      radial-gradient(ellipse at 25% 35%, #e9c2a8 0%, rgba(233,194,168,0) 38%),
      radial-gradient(ellipse at 18% 75%, #c8283c 0%, rgba(200,40,60,0) 30%),
      linear-gradient(135deg, #6f7d3a 0%, #a9a15a 40%, #7b5b3c 70%, #4f5d2c 100%);
  }
  .chevrons { position: absolute; left: 0; top: 0; width: 797px; height: 1200px; }
  .logo-box {
    position: absolute; left: 582px; top: 0; width: 156px; height: 208px;
    background: var(--white); display: flex; flex-direction: column;
    align-items: center; justify-content: flex-end; padding-bottom: 20px; gap: 18px;
  }
  .logo-box .dot { width: 70px; height: 70px; border-radius: 50%; background: var(--sky); }
  .logo-box .name { font-weight: 700; font-size: 34px; letter-spacing: 2px; color: var(--lime); }
  .headline { position: absolute; left: 0; width: 797px; text-align: center; }
  .kicker { font-size: 18.5px; color: var(--lime); letter-spacing: 0.2px; }
  .big-blue { font-size: 44px; font-weight: 900; color: var(--sky); letter-spacing: 0.5px; }
  .big-lime { font-size: 36.5px; font-weight: 900; color: var(--lime); }
  .card { position: absolute; }
  .card-title {
    position: relative; background: var(--sky); color: var(--white);
    font-weight: 700; font-size: 18.5px; line-height: 21px; padding: 0 25px;
    display: flex; align-items: center;
  }
  .card-title::before, .card-title::after {
    content: ""; position: absolute; bottom: -6px; width: 0; height: 0;
    border-top: 6px solid var(--sky-dark);
  }
  .card-title::before { left: 0; border-left: 12px solid transparent; }
  .card-title::after { right: 0; border-right: 12px solid transparent; }
  .card-body {
    background: var(--sky-pale); margin: 0 12px; padding: 12px 13px;
    font-size: 14px; line-height: 16.3px;
    hyphens: auto; -webkit-hyphens: auto;
  }
  .card-body p + p { margin-top: 16px; }
  .donate {
    position: absolute; left: 438px; top: 1022px; width: 312px; height: 88px;
    background: linear-gradient(90deg, #e9c7a7 0%, #f1e4cf 45%, #f6efe2 100%);
  }
  .donate .photo {
    position: absolute; left: 0; top: 0; width: 120px; height: 88px;
    background: linear-gradient(135deg, #e58a7c 0%, #f0c7a6 60%, rgba(240,199,166,0) 100%);
  }
  .donate .copy { position: absolute; right: 10px; top: 11px; text-align: right; }
  .donate .small { font-size: 7px; font-weight: 700; color: var(--red); }
  .donate .big { font-size: 16.5px; font-weight: 900; color: var(--red); line-height: 20px; }
  .donate .ccp { font-size: 5.5px; color: var(--red); margin-top: 2px; }
  .donate .mini-name { font-size: 7px; font-weight: 700; color: var(--lime); margin-top: 14px; margin-right: 46px; }
  .notch { position: absolute; left: 0; top: 0; }
  .footer {
    position: absolute; left: 0; top: 1134px; width: 797px; height: 66px;
    background: var(--orange); font-size: 12.5px; color: var(--ink);
  }
  .footer .item { position: absolute; display: flex; align-items: center; gap: 10px; }
  .footer .divider { position: absolute; top: 10px; width: 1px; height: 46px; background: #6b5a30; }
  .sq { width: 14px; height: 14px; background: var(--ink); }
  .circ { width: 16px; height: 16px; border-radius: 50%; background: var(--ink); }
</style>
</head>
<body>
<div class="poster">
  <div class="hero-photo" role="img" aria-label="Photo d'une petite fille riant sur une balançoire en corde, en plein air"></div>

  <svg class="chevrons" viewBox="0 0 797 1200" aria-hidden="true">
    <polygon points="0,342 398,312 797,342 797,450 0,450" fill="var(--sky)"/>
    <polygon points="0,344 172,392 0,424" fill="var(--lime)"/>
    <polygon points="797,344 625,392 797,424" fill="var(--lime)"/>
    <polygon points="0,446 398,322 797,446 797,460 0,460" fill="var(--white)"/>
  </svg>

  <div class="logo-box">
    <div class="dot"></div>
    <div class="name">YBSN</div>
  </div>

  <div class="headline" style="top:382px"><div class="kicker">AIDEZ-NOUS À CHANGER LA VIE DES</div></div>
  <div class="headline" style="top:400px"><div class="big-blue">ENFANTS VIVANT</div></div>
  <div class="headline" style="top:467px"><div class="kicker">AVEC UN</div></div>
  <div class="headline" style="top:491px"><div class="big-lime">PROBLÈME VESTIBULAIRE</div></div>

  <section class="card" style="left:33px; top:562px; width:335px;">
    <h2 class="card-title" style="height:50px">Qu’est-ce que le vestibule ?</h2>
    <div class="card-body" style="height:82px">C’est un organe sensoriel, pilier de votre équilibre, véritable 6ème sens situé dans l’oreille interne.</div>
  </section>

  <section class="card" style="left:427px; top:562px; width:336px;">
    <h2 class="card-title" style="height:50px">Qu’est ce qu’une aréflexie<br>vestibulaire ?</h2>
    <div class="card-body" style="height:82px">C’est l’absence complète de toute information vestibulaire. L’enfant a ainsi l’impression que tout vacille autour de lui, jour et nuit.</div>
  </section>

  <section class="card" style="left:33px; top:730px; width:335px;">
    <h2 class="card-title" style="height:50px">Quelles en sont les conséquences<br>pour l’enfant ?</h2>
    <div class="card-body" style="height:324px; padding-top:18px">
      <p>Le développement moteur de l’enfant est retardé car il doit trouver des solutions afin de construire son équilibre, stabiliser son regard et son corps.</p>
      <p>Certains apprentissages sont de véritables obstacles pour l’enfant : se représenter son propre corps, se situer dans l’espace qui l’entoure, interagir avec les autres, communiquer, écrire, lire, manger, boire, marcher. Chacune de ces actions necessitent des efforts considérables pour se concentrer quelques secondes ou minutes.</p>
      <p>Quand l’enfant réussit à effectuer l’une de ces actions, son comportement peut sembler déroutant et bien trop souvent mal interprété par le grand public.</p>
    </div>
  </section>

  <section class="card" style="left:427px; top:730px; width:336px;">
    <h2 class="card-title" style="height:50px">Quel est le but de notre<br>association ?</h2>
    <div class="card-body" style="height:226px; padding-top:18px">Notre association a pour but de promouvoir les troubles vestibulaires chez l’enfant, ses conséquences sur sa santé ainsi que celui de son entourage et de soutenir ces enfants et leurs parents en leur offrant un espace de parole et des solutions concrètes pour soulager leur quotidien. Notre association a également pour but de financer et promouvoir toute action de recherche scientifique visant à aider les enfants ayant un trouble vestibulaire.</div>
  </section>

  <div class="donate">
    <div class="photo" role="img" aria-label="Photo d'un bébé portant des lunettes"></div>
    <div class="copy">
      <div class="small">DONATE &amp; HELP US TO</div>
      <div class="big">CHANGE HIS LIFE</div>
      <div class="ccp">CCP : 10-482615-3</div>
      <div class="mini-name">YBSN</div>
    </div>
  </div>

  <svg class="notch" width="797" height="1200" viewBox="0 0 797 1200" aria-hidden="true">
    <polygon points="362,1134 398,1098 434,1134" fill="var(--orange)"/>
  </svg>

  <footer class="footer">
    <div class="item" style="left:74px; top:12px">
      <svg width="14" height="18" viewBox="0 0 14 18" aria-hidden="true"><path d="M7 0C3 0 0 3 0 7c0 5 7 11 7 11s7-6 7-11c0-4-3-7-7-7z" fill="var(--ink)"/><circle cx="7" cy="7" r="2.6" fill="var(--orange)"/></svg>
      <span>Montvert, Valdoria</span>
    </div>
    <div class="divider" style="left:218px"></div>
    <div class="item" style="left:238px; top:13px"><span class="sq"></span><span>community.ybsnetwork.org/groups/parents</span></div>
    <div class="item" style="left:238px; top:40px"><span class="sq"></span><span>https://news.ybsnetwork.org/updates</span></div>
    <div class="divider" style="left:541px"></div>
    <div class="item" style="left:557px; top:12px"><span class="circ"></span><span>www.ybsnetwork.org</span></div>
    <div class="item" style="left:557px; top:39px">
      <svg width="16" height="12" viewBox="0 0 16 12" aria-hidden="true"><rect width="16" height="12" fill="var(--ink)"/><path d="M0 0l8 7 8-7" stroke="var(--orange)" stroke-width="1.4" fill="none"/></svg>
      <span>info@ybsnetwork.org</span>
    </div>
  </footer>
</div>
</body>
</html>
```